Tranquil Pathways Hypnotherapy Business Card

Logo attached. (will be printing onto thick white/off white textured card)

Double sided business card for two Therapists working at Tranquil Pathways Hypnotherapy.

Require one design, but with different name and mobile numbers on each card.

Target Market(s)

Medical, Health

Industry/Entity Type

Business

Contact Information for Business Card

Need one business card design, but a separate card for each person - Darren Whitfield and Marike de Bruyn.

FRONT OF CARD

Logo

Name (Darren Whitfield on one card, Marike de Bruyn on the other)
Professional Clinical Hypnotherapist

Consulting Rooms (Near Larkmoor Hospital)
284 Bellcrest Avenue
Ferncliffe VIC 3162

Darren@TranquilPathwaysHypno.com.au OR Marike@TranquilPathwaysHypno.com.au

Mobile: 0427 862 491 (for Darren) OR
Mobile: 0438 574 206 (for Marike)

BACK OF CARD

Logo

Website: www.TranquilPathwaysHypno.com.au

Phone: 1300 748 519

Requirements
Must have
• Text and logo only. No additiional graphics.

```html
<!DOCTYPE html>
<html lang="en">
<head>
<meta charset="utf-8">
<title>Tranquil Pathways Hypnotherapy – Business Card</title>
<link href="https://fonts.googleapis.com/css2?family=Lato:wght@400;700;900&display=swap" rel="stylesheet">
<style>
  :root {
    --navy: #23296b;
    --navy-soft: #3a3f7e;
    --ink: #4a4a4f;
    --rule: #9a9aa0;
    --card: #f7f7f7;
    --backdrop: #e6e4e0;
  }
  * { box-sizing: border-box; margin: 0; padding: 0; }
  html, body {
    width: 1200px; height: 1024px; overflow: hidden;
    background: var(--backdrop);
    font-family: "Lato", Arial, sans-serif;
    color: var(--ink);
  }
  .canvas {
    width: 1200px; height: 1024px;
    display: flex; flex-direction: column; align-items: center; justify-content: center;
    gap: 56px;
  }
  .card {
    position: relative; width: 770px; height: 440px;
    background: linear-gradient(135deg, #ffffff 0%, var(--card) 60%, #ececec 100%);
    box-shadow: 0 6px 18px rgba(0,0,0,.18);
    overflow: hidden;
  }

  /* brand lockup */
  .brand { display: flex; align-items: center; gap: 16px; }
  .brand-dot {
    width: 64px; height: 64px; border-radius: 50%;
    background: var(--navy); flex: none;
  }
  .brand-name {
    font-weight: 700; color: var(--navy);
    text-transform: uppercase; letter-spacing: 1px; line-height: 1.1;
    border-left: 1px solid var(--rule); padding-left: 16px;
  }

  /* front */
  .front-band {
    position: absolute; left: 0; right: 0; bottom: 0; height: 40px;
  }
  .front .brand { position: absolute; left: 44px; top: 40px; }
  .front .brand-name { font-size: 20px; }
  .holder {
    position: absolute; right: 44px; top: 48px; width: 380px; text-align: right;
  }
  .holder-name {
    font-size: 32px; font-weight: 700; color: var(--navy);
    padding-bottom: 8px; border-bottom: 1px solid var(--rule);
  }
  .holder-title { font-size: 16px; margin-top: 8px; }
  .front-rule {
    position: absolute; left: 44px; top: 186px; width: 330px;
    border-top: 1px solid var(--rule);
  }
  .contact { position: absolute; left: 44px; top: 204px; font-size: 17px; }
  .contact-heading { font-weight: 700; color: var(--navy); font-size: 19px; }
  .contact-sub { color: var(--navy-soft); margin-bottom: 10px; }
  .contact-row { display: flex; align-items: center; gap: 12px; line-height: 30px; }
  .contact-row svg { width: 16px; height: 16px; flex: none; }
  .contact-row.indent { padding-left: 28px; }

  /* back */
  .back-band {
    position: absolute; left: 0; top: 0; bottom: 0; width: 34px; background: var(--navy);
  }
  .back .brand { position: absolute; left: 150px; top: 90px; }
  .back .brand-dot { width: 84px; height: 84px; }
  .back .brand-name { font-size: 28px; padding-left: 20px; }
  .back-rule {
    position: absolute; left: 100px; right: 100px; top: 236px;
    border-top: 1px solid var(--rule);
  }
  .web { position: absolute; left: 100px; top: 258px; font-size: 20px; }
  .phone {
    position: absolute; left: 100px; top: 300px;
    font-size: 40px; font-weight: 700; color: var(--navy); letter-spacing: 1px;
  }
</style>
</head>
<body>
<main class="canvas">

  <section class="card front" aria-label="Card front">
    <svg class="front-band" viewBox="0 0 770 40" preserveAspectRatio="none" aria-hidden="true">
      <polygon points="0,0 580,0 600,22 770,22 770,40 0,40" fill="var(--navy)"/>
    </svg>

    <div class="brand">
      <span class="brand-dot"></span>
      <span class="brand-name">Tranquil Pathways<br>Hypnotherapy</span>
    </div>

    <div class="holder">
      <div class="holder-name">Darren Whitfield</div>
      <div class="holder-title">Professional Clinical Hypnotherapist</div>
    </div>

    <div class="front-rule"></div>

    <div class="contact">
      <div class="contact-heading">Consulting Rooms</div>
      <div class="contact-sub">(Near Larkmoor Hospital)</div>
      <div class="contact-row">
        <svg viewBox="0 0 16 16" aria-hidden="true"><path d="M8 1a5 5 0 0 0-5 5c0 4 5 9 5 9s5-5 5-9a5 5 0 0 0-5-5zm0 7a2 2 0 1 1 0-4 2 2 0 0 1 0 4z" fill="var(--navy)"/></svg>
        <span>284 Bellcrest Avenue</span>
      </div>
      <div class="contact-row indent">Ferncliffe VIC 3162</div>
      <div class="contact-row">
        <svg viewBox="0 0 16 16" aria-hidden="true"><rect x="1" y="3" width="14" height="10" rx="1" fill="var(--navy)"/><path d="M1.5 4 8 9l6.5-5" stroke="#fff" stroke-width="1.2" fill="none"/></svg>
        <span>Darren@TranquilPathwaysHypno.com.au</span>
      </div>
      <div class="contact-row">
        <svg viewBox="0 0 16 16" aria-hidden="true"><rect x="4" y="1" width="8" height="14" rx="1.5" fill="none" stroke="var(--navy)" stroke-width="1.5"/><circle cx="8" cy="12.5" r="0.9" fill="var(--navy)"/></svg>
        <span>0427 862 491</span>
      </div>
    </div>
  </section>

  <section class="card back" aria-label="Card back">
    <div class="back-band"></div>
    <div class="brand">
      <span class="brand-dot"></span>
      <span class="brand-name">Tranquil Pathways<br>Hypnotherapy</span>
    </div>
    <div class="back-rule"></div>
    <div class="web">www.TranquilPathwaysHypno.com.au</div>
    <div class="phone">1300 748 519</div>
  </section>

</main>
</body>
</html>
```